New Template design for Website in Wordpress

We are interested in changing our website look at www.cargolinx.com -We also are very interested in Have it done in Wordpress in which we are understanding the search engines are liking a bit more. The website we would want to try working with on this is www.cargolinx.com. We look forward to seeing the different design ideas please just make sure they are in wordpress! Thanks, Marlen

Reason: need more design idea..... We would still like to use our pictures off our site since we paid for them so keep that in mind as well as we would still want the rotating pictures in the head of the page but not in Flash.

```html
<!DOCTYPE html>
<html lang="en">
<head>
<meta charset="utf-8">
<title>CargoLinx — Freight Quotes</title>
<link href="https://fonts.googleapis.com/css2?family=Open+Sans:ital,wght@0,400;0,600;0,700;0,800;1,400;1,700&family=Oswald:wght@500;600&display=swap" rel="stylesheet">
<style>
:root{
  --page:#e6e8ea;
  --panel:#ffffff;
  --navy:#1e2b38;
  --navy-deep:#151f29;
  --nav:#dfe3e7;
  --blue:#1f8fd6;
  --orange:#f39a1d;
  --red:#d9342b;
  --text:#555c63;
  --muted:#8a9299;
  --foot-text:#aab3bb;
}
*{box-sizing:border-box;margin:0;padding:0}
html,body{width:750px;height:1200px;overflow:hidden}
body{background:var(--page);font-family:"Open Sans",Arial,sans-serif;color:var(--text);font-size:9px}
.site{width:750px;height:1200px;position:relative}
.wrap{width:610px;margin:0 auto}

/* header */
.masthead{height:72px;background:var(--navy)}
.masthead .wrap{display:flex;justify-content:space-between;align-items:center;height:72px}
.brand-name{font-family:"Open Sans",Arial,sans-serif;font-weight:700;font-size:24px;color:#fff;line-height:1}
.brand-tag{font-size:8px;color:#c8d0d7;margin-top:4px}
.hotline{text-align:right}
.hotline-label{font-size:9px;color:var(--blue);font-weight:700;display:flex;align-items:center;gap:4px;justify-content:flex-end}
.hotline-number{font-size:15px;color:var(--blue);font-weight:700;margin-top:2px}

/* nav */
.main-nav{height:28px}
.main-nav ul{list-style:none;display:flex;height:28px;background:var(--nav)}
.main-nav li{font-size:9.5px;font-weight:600;color:#4a535b;padding:0 13px;line-height:28px;border-right:1px solid #c9ced3}
.main-nav li.active{background:var(--blue);color:#fff}
.main-nav li.quote{margin-left:auto;background:var(--blue);color:#fff;font-weight:700;border:none}

/* hero */
.hero{height:398px;position:relative}
.hero-photo{position:absolute;inset:0;background:linear-gradient(180deg,#9fb7cc 0%,#b7c3c9 35%,#8c6a4a 62%,#5d4a3a 100%)}
.hero-copy{position:absolute;left:0;right:0;top:232px;text-align:center}
.hero-title{font-family:"Oswald",Arial,sans-serif;font-weight:600;font-size:30px;color:#fff;letter-spacing:.5px}
.hero-call{font-family:"Oswald",Arial,sans-serif;font-weight:500;font-size:22px;color:var(--orange);margin-top:2px}
.hero-band{position:absolute;left:0;right:0;bottom:22px;height:34px;background:rgba(15,22,30,.82);color:#fff;font-size:12px;font-weight:700;text-align:center;line-height:34px}

/* intro */
.intro{height:170px;background:var(--panel);padding:16px 26px 0;text-align:center}
.intro h1{font-family:"Oswald",Arial,sans-serif;font-weight:600;font-size:19px;color:var(--blue)}
.intro h2{font-size:9px;font-weight:600;color:var(--muted);letter-spacing:1px;margin:2px 0 10px}
.intro p{font-size:7.5px;line-height:1.55;text-align:left;margin-bottom:5px}
.intro .cta{font-style:italic;font-weight:700;color:#333;font-size:8.5px;text-align:center;margin-top:6px}
.intro .cta span{color:var(--blue)}

/* services */
.services{height:198px;background:var(--panel);padding:6px 22px 0}
.section-title{font-family:"Oswald",Arial,sans-serif;font-weight:600;font-size:17px;color:var(--red);text-align:center;margin-bottom:10px}
.section-title.blue{color:var(--blue)}
.service-grid{display:grid;grid-template-columns:repeat(4,1fr);gap:16px}
.service-photo{height:78px}
.photo-haul{background:linear-gradient(160deg,#d9b64a,#8c7a55)}
.photo-reefer{background:linear-gradient(160deg,#cdd6de,#7d8d9c)}
.photo-flat{background:linear-gradient(160deg,#b9c7d4,#5d7288)}
.photo-forward{background:linear-gradient(160deg,#a9c3da,#3e6488)}
.service h3{font-size:9px;font-weight:800;color:#2b3138;text-align:center;margin:8px 0 3px}
.service p{font-size:7px;line-height:1.45;text-align:center;color:var(--muted)}

/* news */
.news{height:134px;background:var(--page);padding:12px 22px 0}
.news-grid{display:grid;grid-template-columns:repeat(3,1fr);gap:18px}
.news-item{display:flex;gap:8px}
.news-date{text-align:center;color:var(--blue);width:34px;flex:none}
.news-date .day{font-size:24px;font-weight:300;line-height:1}
.news-date .month{font-size:11px;border-top:1px solid var(--blue);margin-top:3px;padding-top:2px}
.news-item p{font-size:7px;line-height:1.5;color:var(--muted)}
.news-item .more{display:block;text-align:right;color:var(--blue);font-weight:700;font-size:7px;margin-top:4px}

/* footer */
.footer{height:168px;background:var(--navy)}
.footer .wrap{display:grid;grid-template-columns:repeat(3,1fr);gap:20px;padding:16px 24px 0}
.footer h4{font-size:9px;font-weight:800;color:#fff;margin-bottom:8px}
.footer ul{list-style:none}
.footer li{font-size:7.5px;color:var(--foot-text);line-height:15px}
.footer li::before{content:"» ";color:var(--blue)}
.footer li.current{color:var(--blue)}
.legal{height:32px;background:var(--navy-deep)}
.legal .wrap{padding:6px 24px;font-size:7px;color:#7d8790;line-height:10px}
</style>
</head>
<body>
<div class="site">
  <header class="masthead">
    <div class="wrap">
      <div class="brand">
        <div class="brand-name">CargoLinx</div>
        <div class="brand-tag">Trucking and Ocean Shipping</div>
      </div>
      <div class="hotline">
        <div class="hotline-label">
          <svg width="9" height="9" viewBox="0 0 24 24"><path fill="#1f8fd6" d="M6.6 10.8a15 15 0 0 0 6.6 6.6l2.2-2.2c.3-.3.7-.4 1-.2 1.1.4 2.3.6 3.6.6.6 0 1 .4 1 1V20c0 .6-.4 1-1 1A17 17 0 0 1 3 4c0-.6.4-1 1-1h3.5c.6 0 1 .4 1 1 0 1.3.2 2.5.6 3.6.1.3 0 .7-.2 1z"/></svg>
          24 HOURS A WEEK CALL
        </div>
        <div class="hotline-number">(555) 014-2290</div>
      </div>
    </div>
  </header>

  <nav class="main-nav">
    <ul class="wrap">
      <li class="active">HOME</li>
      <li>ABOUT US</li>
      <li>SERVICES</li>
      <li>INSURANCE &amp; LEGAL INFO</li>
      <li>CONTACT US</li>
      <li class="quote">FAST FREIGHT QUOTE</li>
    </ul>
  </nav>

  <section class="hero wrap">
    <div class="hero-photo" role="img" aria-label="Container ship loaded with stacked cargo containers at port"></div>
    <div class="hero-copy">
      <div class="hero-title">GET FAST &amp; FREE FREIGHT QUOTES</div>
      <div class="hero-call">24/7 WEEK CALL - (555) 014-2290</div>
    </div>
    <div class="hero-band">Worldwide Shipping - Trucking and Ocean Service with No Limits - Click Here for Freight Quote</div>
  </section>

  <section class="intro wrap">
    <h1>GET FAST &amp; FREE FREIGHT QUOTES NOW AND SAVE!!</h1>
    <h2>WORLDWIDE SHIPPING, OCEAN AND TRUCKING WITH NO LIMITS</h2>
    <p>Welcome to CargoLinx and www.cargolinx.com. We are a one stop solution logistics company servicing the world with our trucking and ocean shipping services. In using our freight services we will negotiate a competitive freight quote using over 5000 different carriers who are certified and contracted by us. We have all equipment types available daily, across all freight types, and have no time restrictions.</p>
    <p>Whether you need a freight quote for standard LTL, full truck load, oversized machinery or equipment, trucking and/or ocean shipment, we will take care of it. All your freight is insured and tracked from pickup to delivery by our trusted team, with no limitations on weight, size or distance, and with the right carrier matched to every load.</p>
    <p class="cta">Get your <span>freight quote online now</span> or call (555) 014-2290 and save with one of the top carriers in the country compete for your business</p>
  </section>

  <section class="services wrap">
    <h2 class="section-title">OUR SERVICES</h2>
    <div class="service-grid">
      <div class="service">
        <div class="service-photo photo-haul" role="img" aria-label="Heavy excavator loaded for hauling"></div>
        <h3>HEAVY HAUL</h3>
        <p>No Limits on Equipment Weight and Size - All Machinery</p>
      </div>
      <div class="service">
        <div class="service-photo photo-reefer" role="img" aria-label="Refrigerated semi truck on the highway"></div>
        <h3>DRY &amp; REFRIGERATED</h3>
        <p>Dry Van Freight Quotes servicing All States &amp; Canada</p>
      </div>
      <div class="service">
        <div class="service-photo photo-flat" role="img" aria-label="Flatbed truck carrying steel load"></div>
        <h3>FLATBED, STEP DECK</h3>
        <p>Shipping LTL Freight throughout All States &amp; Canada</p>
      </div>
      <div class="service">
        <div class="service-photo photo-forward" role="img" aria-label="Cargo ship at sea for freight forwarding"></div>
        <h3>FREIGHT FORWARDING</h3>
        <p>Shipping LTL Freight through All States &amp; Canada</p>
      </div>
    </div>
  </section>

  <section class="news wrap">
    <h2 class="section-title blue">LATEST NEWS</h2>
    <div class="news-grid">
      <article class="news-item">
        <div class="news-date"><div class="day">22</div><div class="month">08</div></div>
        <div><p>New lane added for weekly flatbed runs across the southern states.</p><span class="more">READ MORE »</span></div>
      </article>
      <article class="news-item">
        <div class="news-date"><div class="day">22</div><div class="month">08</div></div>
        <div><p>Ocean freight rates updated for the coming season on all routes.</p><span class="more">READ MORE »</span></div>
      </article>
      <article class="news-item">
        <div class="news-date"><div class="day">22</div><div class="month">08</div></div>
        <div><p>Our online quote form now returns carrier prices in minutes.</p><span class="more">READ MORE »</span></div>
      </article>
    </div>
  </section>

  <footer class="footer">
    <div class="wrap">
      <div>
        <h4>WORLDWIDE FREIGHT SERVICES</h4>
        <ul>
          <li class="current">Worldwide Shipping to you</li>
          <li>Trucking Shipping Services</li>
          <li>Ocean Shipping Services</li>
          <li>Insurance &amp; Legal Details</li>
          <li>Get a Freight Quote Now</li>
          <li>Return to Home Page</li>
          <li>Equipment Transport</li>
        </ul>
      </div>
      <div>
        <h4>FREIGHT - TRUCKING SERVICE</h4>
        <ul>
          <li>Heavy Equipment Hauling</li>
          <li>LTL Freight Shipping</li>
          <li>Flatbed Transport</li>
          <li>Step Deck Transport</li>
          <li>Dry Van Transport</li>
          <li>Refrigerated Transport</li>
          <li>Power Only &amp; Tradeshow Freight</li>
        </ul>
      </div>
      <div>
        <h4>WE SHIP IT ALL WORLDWIDE!</h4>
        <ul>
          <li>Full Loads</li>
          <li>LTL Less Than Full Loads</li>
          <li>Oversized &amp; Overweight Loads</li>
          <li>RV, Boats &amp; Vehicles</li>
          <li>Construction &amp; Mining Equipment</li>
          <li>Farm &amp; Machinery</li>
          <li>Tanks, Metal Equipment and More</li>
        </ul>
      </div>
    </div>
  </footer>
  <div class="legal">
    <div class="wrap">Equipment Transport | Equipment Hauling | Shipping Service Index<br>Copyright © 2014 CargoLinx, All Rights Reserved</div>
  </div>
</div>
</body>
</html>
```